letterhead and vector data for stamp ( i already have a example of what i want)

i need a letterhead (with logo) and a vector data to create a stamp.

it should be possible to use with openoffice and should look printed out very good.

the stamp data should be a vector how was priovsly descriped to me. so i need to do a stamp and need the data for it. i already have a example

Logo Text

eagle

Requirements
Must have
• logo and adress website and company name
Nice to have
• eagle logo
Should not have
• colourful logo or shadows

```html
<!DOCTYPE html>
<html lang="de">
<head>
<meta charset="utf-8">
<title>Briefbogen und Stempel – Botschaft der Republik Veldmark</title>
<link href="https://fonts.googleapis.com/css2?family=Didact+Gothic&display=swap" rel="stylesheet">
<style>
  :root {
    --backdrop: #b4bbbd;
    --paper: #f1f1f1;
    --ink: #222222;
    --ink-soft: #6a6a6a;
    --crest-line: #9a9a9a;
    --stamp: #5b3a86;
    --stamp-fill: #d9d0e4;
  }
  html, body {
    margin: 0;
    width: 1200px;
    height: 1000px;
    overflow: hidden;
    background: var(--backdrop);
    font-family: "Didact Gothic", "Century Gothic", sans-serif;
  }
  .canvas {
    position: relative;
    width: 1200px;
    height: 1000px;
  }
  .sheet {
    position: absolute;
    top: 124px;
    width: 528px;
    height: 746px;
    background: var(--paper);
  }
  .sheet--color { left: 49px; }
  .sheet--mono { left: 625px; }

  .letterhead {
    position: absolute;
    top: 19px;
    left: 0;
    right: 0;
    text-align: center;
    color: var(--ink);
    font-size: 9.5px;
    line-height: 10.5px;
  }
  .letterhead__mark {
    display: block;
    width: 40px;
    height: 44px;
    margin: 0 auto 12px;
    box-sizing: border-box;
    border: 1px solid var(--crest-line);
    border-radius: 2px;
  }
  .letterhead__name { margin: 0; }
  .letterhead__department { margin: 5px 0 0; }

  .stamp {
    position: absolute;
    left: 348px;
    top: 601px;
    width: 80px;
    height: 80px;
  }
  .stamp text {
    font-family: "Didact Gothic", "Century Gothic", sans-serif;
    fill: var(--stamp);
  }
  .stamp__outer-text { font-size: 7px; }
  .stamp__inner-text { font-size: 5.6px; }

  .contact {
    position: absolute;
    left: 0;
    right: 0;
    bottom: 22px;
    margin: 0;
    text-align: center;
    font-size: 7.5px;
    color: var(--ink-soft);
  }
</style>
</head>
<body>
<main class="canvas">
  <section class="sheet sheet--color" aria-label="Briefbogen, Farbversion">
    <header class="letterhead">
      <span class="letterhead__mark"></span>
      <p class="letterhead__name">Botschaft<br>der Republik Veldmark</p>
      <p class="letterhead__department">Konsularabteilung</p>
    </header>
    <svg class="stamp" viewBox="0 0 80 80" aria-label="Stempel der Konsularabteilung">
      <defs>
        <path id="ring-outer-a" d="M40,69 A29,29 0 1,1 40,11 A29,29 0 1,1 40,69"/>
        <path id="ring-inner-a" d="M40,61 A21,21 0 1,1 40,19 A21,21 0 1,1 40,61"/>
      </defs>
      <circle cx="40" cy="40" r="38.5" fill="none" stroke="var(--stamp)" stroke-width="1.2"/>
      <circle cx="40" cy="40" r="36.6" fill="none" stroke="var(--stamp)" stroke-width="0.5"/>
      <text class="stamp__outer-text"><textPath href="#ring-outer-a" startOffset="10" textLength="162" lengthAdjust="spacing">Botschaft der Republik Veldmark</textPath></text>
      <text class="stamp__inner-text" text-anchor="middle"><textPath href="#ring-inner-a" startOffset="50%">Konsularabteilung</textPath></text>
      <circle cx="40" cy="40" r="18" fill="none" stroke="var(--stamp)" stroke-width="0.6"/>
      <circle cx="40" cy="41" r="12" fill="var(--stamp-fill)" role="img" aria-label="Wappen im Stempelfeld"/>
      <path d="M40,67.2 l0.9,1.9 2,0.2 -1.5,1.3 0.5,2 -1.9,-1.1 -1.9,1.1 0.5,-2 -1.5,-1.3 2,-0.2z" fill="var(--stamp)"/>
    </svg>
    <p class="contact">Musterallee 12 · 3006 Bern · Tel. +41 31 000 00 00 · www.veldmark-botschaft.example</p>
  </section>

  <section class="sheet sheet--mono" aria-label="Briefbogen, Graustufenversion">
    <header class="letterhead">
      <span class="letterhead__mark"></span>
      <p class="letterhead__name">Botschaft<br>der Republik Veldmark</p>
      <p class="letterhead__department">Konsularabteilung</p>
    </header>
    <svg class="stamp" viewBox="0 0 80 80" aria-label="Stempel der Konsularabteilung">
      <defs>
        <path id="ring-outer-b" d="M40,69 A29,29 0 1,1 40,11 A29,29 0 1,1 40,69"/>
        <path id="ring-inner-b" d="M40,61 A21,21 0 1,1 40,19 A21,21 0 1,1 40,61"/>
      </defs>
      <circle cx="40" cy="40" r="38.5" fill="none" stroke="var(--stamp)" stroke-width="1.2"/>
      <circle cx="40" cy="40" r="36.6" fill="none" stroke="var(--stamp)" stroke-width="0.5"/>
      <text class="stamp__outer-text"><textPath href="#ring-outer-b" startOffset="10" textLength="162" lengthAdjust="spacing">Botschaft der Republik Veldmark</textPath></text>
      <text class="stamp__inner-text" text-anchor="middle"><textPath href="#ring-inner-b" startOffset="50%">Konsularabteilung</textPath></text>
      <circle cx="40" cy="40" r="18" fill="none" stroke="var(--stamp)" stroke-width="0.6"/>
      <circle cx="40" cy="41" r="12" fill="var(--stamp-fill)" role="img" aria-label="Wappen im Stempelfeld"/>
      <path d="M40,67.2 l0.9,1.9 2,0.2 -1.5,1.3 0.5,2 -1.9,-1.1 -1.9,1.1 0.5,-2 -1.5,-1.3 2,-0.2z" fill="var(--stamp)"/>
    </svg>
    <p class="contact">Musterallee 12 · 3006 Bern · Tel. +41 31 000 00 00 · www.veldmark-botschaft.example</p>
  </section>
</main>
</body>
</html>
```